Classy, Elegant, Simple Business Card Design

Looking to have a classy, simple, and elegant design. Want a top notch designed business card. I really like the look of the new brivo credit card. I also like the design I attached. I am trying to reach 21-29 year old females for booking us for there wedding or event. We offer Disc Jockey Service, Photo Booth Rentals, and Uplighting .

Target Market(s)

21-28 year old females

Contact Information for Business Card

Has to have logo, website, email, and phone number

Font styles to use
Other font styles liked:
• open to font choice, modern, clean
Designer to choose
33a6d7
0791cd
0555a3
ffffff

Requirements
Must have
• Has to have logo, website, email, and phone number
Nice to have
• I really like the design of the new brivo credit card. I also included my logo and some designs I like
Should not have
• clutter or too much info

```html
<!DOCTYPE html>
<html lang="en">
<head>
<meta charset="utf-8">
<title>Tidelight Event Group — Business Card</title>
<link rel="stylesheet" href="https://fonts.googleapis.com/css2?family=Questrial&display=swap">
<style>
  :root {
    --bg: #3a3b3e;
    --card: #0b0c0f;
    --blue-light: #33a6d7;
    --blue: #0791cd;
    --blue-deep: #0555a3;
    --white: #ffffff;
    --muted: #c9ccd2;
  }
  * { margin: 0; padding: 0; box-sizing: border-box; }
  html, body {
    width: 1200px;
    height: 900px;
    overflow: hidden;
    background: var(--bg);
    font-family: "Questrial", "Century Gothic", sans-serif;
  }
  .sheet {
    width: 1200px;
    height: 900px;
    display: flex;
    flex-direction: column;
    align-items: center;
    justify-content: center;
    gap: 48px;
  }
  .card {
    position: relative;
    width: 640px;
    height: 366px;
    background: var(--card);
    border-radius: 30px;
    box-shadow: 0 14px 30px rgba(0, 0, 0, 0.45);
    overflow: hidden;
  }
  .brand {
    display: flex;
    align-items: center;
    gap: 14px;
    color: var(--blue);
  }
  .brand-dot {
    width: 22px;
    height: 22px;
    border-radius: 50%;
    background: var(--blue);
    flex: none;
  }
  .brand-name {
    font-size: 30px;
    letter-spacing: 0.14em;
    text-transform: uppercase;
    white-space: nowrap;
  }
  .card--front {
    display: flex;
    align-items: center;
    justify-content: center;
  }
  .card--back .brand {
    position: absolute;
    left: 52px;
    top: 56px;
    gap: 10px;
  }
  .card--back .brand-dot { width: 16px; height: 16px; }
  .card--back .brand-name { font-size: 21px; }
  .contact {
    position: absolute;
    left: 52px;
    bottom: 52px;
    list-style: none;
  }
  .contact-rule {
    width: 16px;
    height: 2px;
    background: var(--blue);
    margin-bottom: 16px;
  }
  .contact-item {
    display: flex;
    align-items: center;
    gap: 12px;
    color: var(--white);
    font-size: 17px;
    letter-spacing: 0.02em;
    line-height: 1;
    margin-top: 13px;
  }
  .contact-icon {
    width: 15px;
    height: 15px;
    flex: none;
    fill: none;
    stroke: var(--blue-light);
    stroke-width: 1.8;
    stroke-linecap: round;
    stroke-linejoin: round;
  }
</style>
</head>
<body>
<main class="sheet">
  <section class="card card--front">
    <div class="brand">
      <span class="brand-dot"></span>
      <span class="brand-name">Tidelight Event Group</span>
    </div>
  </section>

  <section class="card card--back">
    <div class="brand">
      <span class="brand-dot"></span>
      <span class="brand-name">Tidelight Event Group</span>
    </div>
    <ul class="contact">
      <li class="contact-rule"></li>
      <li class="contact-item">
        <svg class="contact-icon" viewBox="0 0 24 24" aria-hidden="true"><path d="M5 3h4l2 5-2.5 1.5a11 11 0 0 0 6 6L16 13l5 2v4a2 2 0 0 1-2 2A16 16 0 0 1 3 5a2 2 0 0 1 2-2z"/></svg>
        <span>+1 555 210 4417</span>
      </li>
      <li class="contact-item">
        <svg class="contact-icon" viewBox="0 0 24 24" aria-hidden="true"><rect x="3" y="5" width="18" height="14" rx="1"/><path d="M3 6l9 7 9-7"/></svg>
        <span>info@tidelightevents.com</span>
      </li>
      <li class="contact-item">
        <svg class="contact-icon" viewBox="0 0 24 24" aria-hidden="true"><circle cx="12" cy="12" r="9"/><path d="M3 12h18M12 3a14 14 0 0 1 0 18M12 3a14 14 0 0 0 0 18"/></svg>
        <span>www.tidelightevents.com</span>
      </li>
    </ul>
  </section>
</main>
</body>
</html>
```